Vantrell Law Letterhead

We need a new letterhead design for a Law Firm. The address for the law firm is 4817 Larkspur Boulevard, Suite 250, Houston, Texas 77342. Phone Number: 832-619-3057; Fax Number: 832-407-1694. The logo is uploaded to the project.

```html
<!DOCTYPE html>
<html lang="en">
<head>
<meta charset="utf-8">
<title>Vantrell Law Letterhead</title>
<link href="https://fonts.googleapis.com/css2?family=Montserrat:wght@300;400;500&family=Tinos&display=swap" rel="stylesheet">
<style>
  :root {
    --navy: #1b2f5e;
    --navy-deep: #13264f;
    --red: #e0262b;
    --ink: #333333;
    --muted: #8a8a8a;
    --body: #7a7a7a;
    --backdrop: #e4e5e7;
    --paper: #ffffff;
  }
  * { margin: 0; padding: 0; box-sizing: border-box; }
  html, body { width: 1200px; height: 1200px; overflow: hidden; background: var(--backdrop); }
  .canvas { position: relative; width: 1200px; height: 1200px; }
  .letterhead {
    position: absolute; left: 189.6px; top: 20px;
    width: 934px; height: 1320px;
    background: var(--paper);
    transform: scale(0.8788); transform-origin: top left;
    font-family: "Montserrat", sans-serif;
    box-shadow: 0 2px 10px rgba(0,0,0,0.12);
  }
  .header-band { position: absolute; left: 0; top: 0; width: 934px; height: 60px; }
  .brand { position: absolute; left: 48px; top: 58px; display: flex; align-items: center; gap: 16px; }
  .brand-mark { width: 58px; height: 58px; background: var(--navy); }
  .brand-name { font-size: 32px; font-weight: 500; color: var(--navy); letter-spacing: 0.5px; }
  .recipient { position: absolute; left: 95px; top: 294px; }
  .recipient-label { font-size: 16px; letter-spacing: 3px; color: var(--ink); }
  .recipient-name { margin-top: 8px; font-size: 15.5px; color: var(--red); }
  .recipient-lines { margin-top: 6px; font-size: 13px; line-height: 20.5px; color: var(--muted); font-weight: 300; }
  .letter-date { position: absolute; right: 94px; top: 293px; font-size: 13px; color: var(--ink); }
  .letter-body { position: absolute; left: 95px; top: 471px; width: 747px; font-size: 13.6px; line-height: 16.6px; color: var(--body); font-weight: 300; text-align: justify; }
  .letter-body p { margin-bottom: 16.6px; }
  .signature { position: absolute; left: 95px; top: 935px; width: 165px; height: 36px;
    background: linear-gradient(90deg, rgba(40,40,40,0.18), rgba(40,40,40,0.06)); border-radius: 18px; }
  .signer { position: absolute; left: 93px; top: 982px; }
  .signer-name { font-size: 15px; color: var(--ink); }
  .signer-role { margin-top: 3px; font-size: 12px; color: var(--muted); font-weight: 300; }
  .footer { position: absolute; left: 0; top: 1252px; width: 934px; text-align: center; font-family: "Tinos", serif; color: var(--navy-deep); }
  .footer-contacts { font-size: 15px; display: flex; justify-content: center; align-items: center; gap: 6px; }
  .footer-contacts svg { width: 13px; height: 13px; fill: var(--red); }
  .footer-contacts .gap { width: 2px; }
  .footer-address { margin-top: 6px; font-size: 15.5px; }
</style>
</head>
<body>
<div class="canvas">
  <div class="letterhead">
    <svg class="header-band" viewBox="0 0 934 60" aria-hidden="true">
      <rect x="0" y="0" width="934" height="24" fill="var(--navy)"/>
      <polygon points="0,27 345,27 347,30 0,30" fill="var(--navy-deep)"/>
      <polygon points="0,31 332,31 358,56 372,56 346,31 346,31 340,31 340,37 0,37" fill="var(--red)"/>
      <polygon points="0,31 340,31 366,56 348,56 326,37 0,37" fill="var(--red)"/>
      <polygon points="362,24 382,24 408,46 388,46" fill="var(--navy)"/>
      <polygon points="400,24 934,24 934,46 424,46" fill="var(--navy)"/>
      <rect x="376" y="51" width="558" height="5" fill="var(--navy)"/>
    </svg>

    <div class="brand">
      <div class="brand-mark"></div>
      <div class="brand-name">Vantrell Law</div>
    </div>

    <div class="recipient">
      <div class="recipient-label">TO</div>
      <div class="recipient-name">Dara Quillfen</div>
      <div class="recipient-lines">
        Human Resources<br>
        Northbrook Systems Inc.<br>
        2231-B Halvern Road, Easton<br>
        E89 USA
      </div>
    </div>
    <div class="letter-date">Friday, 01/01/2018</div>

    <div class="letter-body">
      <p>Lorem ipsum dolor sit amet, consectetuer adipiscing elit, sed diam nonmmy nibh euismod tincidunt ut laoreet dolore magna aliquam erat volutpat. Ut wisi enim ad minim veniam, quis nostrud exerci tationmcorper suscipit lobortis nisl ut aliquip ex ea commodo consequat. Duis autem vel eum iriure dolor in hendrerit in vulputate velit esse molestie consequat, vel illum dolore eu feugiat nulla facilisis at vero eros et accumsan et iusto odio dignissim qui blandit praesent luptatum zzril delenit augue duis dolore te feugait nulla facilisi.</p>
      <p>Nam liber tempor cum soluta nobis eleifend option congue nihil imprdiet doming id quod mazim placerat facer possim assum. Typi non habent claritatem insitam;</p>
      <p>Est usus legentis in iis qui facit eorum claritatem.</p>
      <p>Investigationes demonstraverunt lectores legere me lius quod ii legunt saepius. Claritas est etiam processus dynamicus, qui sequitur mutationem consuetudium lectorum. Mirum est notare quam littera gothica, quam nunc putamus parum claram, anteposuerit litterarum formas humanitatis per seacula quarta decima et quinta decima. Eodem modo typi, qui nunc nobis videntur parum clari, fiant sollemnes in futurum.</p>
      <p>consectetuer adipiscing elit, sed diam nonummy nibh euismod tincidunt ut laoreet dolore magna aliquam erat volutpat. Ut wisi enim ad minim veniam, quis nostrud exerci tation ullamcorper suscipit lobortis nisl ut aliquip ex ea commodo consequat. Duis autem vel eum iriure dolor in hendrerit in vulputate velit esse molestie consequat, vel illum dolore eu feugiat nulla facilisis at vero eros et accumsan et iusto odio dignissim qui blandit praesent luptatum zzril delenit augue duis dolore te feugait nulla facilisi.</p>
      <p>Nam liber tempor cum soluta nobis eleifend option congue nihil imperdiet .</p>
    </div>

    <div class="signature" role="img" aria-label="Handwritten signature of Elliot Marrow"></div>
    <div class="signer">
      <div class="signer-name">Elliot Marrow</div>
      <div class="signer-role">Managing Director</div>
    </div>

    <div class="footer">
      <div class="footer-contacts">
        <svg viewBox="0 0 24 24" aria-hidden="true"><path d="M6.6 10.8a15.1 15.1 0 0 0 6.6 6.6l2.2-2.2a1 1 0 0 1 1-.25 11.4 11.4 0 0 0 3.6.57 1 1 0 0 1 1 1V20a1 1 0 0 1-1 1A17 17 0 0 1 3 4a1 1 0 0 1 1-1h3.5a1 1 0 0 1 1 1c0 1.25.2 2.45.57 3.57a1 1 0 0 1-.25 1z"/></svg>
        <span>832-619-3057</span>
        <span class="gap"></span>
        <svg viewBox="0 0 24 24" aria-hidden="true"><path d="M6 2h10v5H6zM3 8h18a1 1 0 0 1 1 1v8h-4v4H6v-4H2V9a1 1 0 0 1 1-1zm5 8v3h8v-3z"/></svg>
        <span>832-407-1694</span>
      </div>
      <div class="footer-address">4817 Larkspur Boulevard, Suite 250, Houston, Texas 77342</div>
    </div>
  </div>
</div>
</body>
</html>
```